Brochure design for Velicor

Create a bi-fold A5 size brochure. I have attached our logo and the written content to be included in the brochure. So the brochure will have a total of 4 pages (front page, inner two pages, back page). End source files need to include final printable brochure as well as editable files.

```html
<!DOCTYPE html>
<html lang="en">
<head>
<meta charset="utf-8">
<title>Velicor – Bi-fold Brochure Outer Spread</title>
<link rel="stylesheet" href="https://fonts.googleapis.com/css2?family=Open+Sans:wght@400;700&family=Fira+Sans:wght@600&display=swap">
<style>
  :root {
    --page-bg: #e9e6e1;
    --deep-blue: #0b5a9c;
    --mid-blue: #1f6fb8;
    --dna-blue: #2f4fc4;
    --sky: #b9d3e6;
    --accent-green: #8cc63f;
    --charcoal: #2b2a2a;
    --brand-blue: #1b5ea6;
    --white: #ffffff;
  }
  * { box-sizing: border-box; margin: 0; padding: 0; }
  html, body { width: 1200px; height: 1200px; overflow: hidden; }
  body {
    background: var(--page-bg);
    font-family: "Open Sans", sans-serif;
    position: relative;
  }
  .spread {
    position: absolute;
    left: 0; top: 175px;
    width: 1200px; height: 849px;
    overflow: hidden;
  }
  .page { position: absolute; top: 0; height: 849px; width: 600px; }
  .page--back { left: 0; }
  .page--front { left: 600px; }

  .dna-visual { position: absolute; inset: 0; }
  .page--back .dna-visual {
    background:
      radial-gradient(ellipse 60% 40% at 70% 70%, rgba(47,79,196,.55), transparent 70%),
      linear-gradient(180deg, var(--deep-blue) 0%, #1869ad 50%, #2a73b4 100%);
  }
  .page--front .dna-visual {
    background:
      radial-gradient(ellipse 45% 55% at 45% 40%, rgba(47,79,196,.85), transparent 70%),
      radial-gradient(ellipse 40% 30% at 80% 20%, rgba(47,79,196,.6), transparent 70%),
      linear-gradient(180deg, #cfe0ec 0%, var(--sky) 35%, #5c8fc0 70%, #2d5fa8 100%);
  }

  .bands { position: absolute; left: 0; top: 0; width: 1200px; height: 849px; }

  .back-info {
    position: absolute; left: 48px; top: 50px; width: 508px;
    color: var(--white);
  }
  .back-info p { font-size: 14.2px; line-height: 16px; }
  .back-info .retailers { margin-top: 16px; }
  .references {
    list-style: none; margin-top: 14px;
    font-size: 10.4px; line-height: 12.4px; letter-spacing: -.2px;
  }
  .references li { padding-left: 18px; text-indent: -18px; }
  .footnote { font-size: 10.4px; line-height: 13px; }

  .wordmark {
    position: absolute; display: flex; align-items: center; gap: 8px;
    font-family: "Open Sans", sans-serif; font-weight: 700;
  }
  .wordmark .dot { border-radius: 50%; }
  .wordmark--back { left: 48px; top: 697px; color: var(--white); font-size: 29px; }
  .wordmark--back .dot { width: 22px; height: 22px; background: var(--white); }
  .back-contact {
    position: absolute; left: 48px; top: 760px;
    color: var(--white); font-size: 14.5px;
  }

  .front-headline {
    position: absolute; left: 48px; top: 458px; width: 500px;
    font-family: "Fira Sans", sans-serif; font-weight: 600;
    color: var(--white); font-size: 18.5px; line-height: 25px;
  }
  .front-headline p + p { margin-top: 24px; }
  .wordmark--front { left: 330px; top: 708px; color: var(--brand-blue); font-size: 44px; }
  .wordmark--front .dot { width: 30px; height: 30px; background: var(--accent-green); }
</style>
</head>
<body>
  <div class="spread">
    <section class="page page--back">
      <div class="dna-visual" role="img" aria-label="Blue DNA double helix photograph on a deep blue background"></div>
      <div class="back-info">
        <p>For more information about <strong>Velicor</strong>™ or our products, please talk to your local retailer or email us at <strong>enquiries@velicor.co</strong><br>Please note test availability may differ from region to region and is subject to availability. Please talk to your local retailer for more information.</p>
        <p class="retailers">For a list of approved <strong>Velicor</strong>™ retailers please visit www.velicor.co</p>
        <ol class="references">
          <li>1.&nbsp;&nbsp; Hale R, et al. Completion of the human genome sequence. Genome Review 2004;12(3):101-118.</li>
          <li>2.&nbsp;&nbsp; Moreau T, Lindqvist P. Clinical use of pharmacogenetic testing. Mol Med Trends 2001;7:201-204.</li>
          <li>3.&nbsp;&nbsp; Okafor J, et al. Pharmacogenetics 1998;8:283-289.</li>
          <li>4.&nbsp;&nbsp; Brandt Y, et al. Journal of Molecular Testing 2016;18(3):438-45.</li>
          <li>5.&nbsp;&nbsp; Castell W, et al. Clinical Pharmacology Reports 2016;100(2):160-9.</li>
          <li>6.&nbsp;&nbsp; Ramesh N, et al. Personalised Medicine Review 2017;27(10):17-27.</li>
          <li>7.&nbsp;&nbsp; Vos SL, et al. Clinical Pharmacology Reports 2014;95(4):423-31.</li>
          <li>8.&nbsp;&nbsp; Pereira A, et al. Food elimination guided by IgG antibodies in irritable bowel syndrome: a randomised controlled trial. Gut Health 2004;53:1459-1464.</li>
          <li>9.&nbsp;&nbsp; Lowell K, et al. Randomised controlled trial of an IgG-based elimination diet for migraine-like headaches. Nutrition Research 2011;10:85.</li>
          <li>10. Duarte CM, Silva PM, Reyes HL. Food allergy mediated by IgG antibodies in adults with migraine. Allergy Review 2007;54:162-8.</li>
          <li>11. Marin C, Fabbri C, Rossi F. Immune complexes in food-induced joint pain. Allergy Annals 1987;59:422-8.</li>
        </ol>
        <p class="footnote">* Additional fees may apply.</p>
      </div>
      <div class="wordmark wordmark--back"><span class="dot"></span>Velicor</div>
      <p class="back-contact">enquiries@velicor.co &nbsp;|&nbsp; www.velicor.co</p>
    </section>

    <section class="page page--front">
      <div class="dna-visual" role="img" aria-label="Close-up photograph of a blue DNA double helix against a pale blue background"></div>
      <div class="front-headline">
        <p>A revolution in health &amp; wellness has been brewing<br>– and now it is here!</p>
        <p>Precision health and wellness is tailored<br>to your unique genetic make-up.</p>
      </div>
    </section>

    <svg class="bands" viewBox="0 0 1200 849" aria-hidden="true">
      <defs>
        <linearGradient id="gutter-shade" x1="0" x2="1" y1="0" y2="0">
          <stop offset="0" stop-color="#ffffff"/>
          <stop offset="0.75" stop-color="#ececec"/>
          <stop offset="1" stop-color="#cfcfcf"/>
        </linearGradient>
      </defs>
      <polygon points="345,849 1085,589 1125,597 1200,622 1200,849" fill="var(--white)"/>
      <polygon points="345,849 600,759 600,849" fill="url(#gutter-shade)"/>
      <polygon points="209,849 1050,578 1085,589 345,849" fill="var(--accent-green)"/>
      <polygon points="1050,578 1100,566 1125,597 1085,589" fill="var(--charcoal)"/>
      <polygon points="1100,566 1122,556 1200,600 1200,622 1125,597" fill="var(--mid-blue)"/>
    </svg>

    <div class="wordmark wordmark--front" style="left:930px;"><span class="dot"></span>Velicor</div>
  </div>
</body>
</html>
```